Design for a 3-4 screens mobile app

The app is a "simple" ordering mobile app.
1. START screen : user can select either "NEW order" either "VIEW history" - or, can access the usual Contact, About, and Conditions pages.
2. NEW order : is a sequence of 3 basic screens/forms made of 3-4 fields each. Logic is the following: you select the service you need, its recurrence, mention where you are located and then you post it towards the marketplace...
3. VIEW history : is where you land at the end of the ordering process - and accessible from START screen. You see there your previous orders, and their statuses.
Mandatory : we need design for START screen, NEW order and VIEW history screens.
Design but be optimized for Smartphones, used in Portrait mode.
Please take into account the design of the website promoting the Mobile App: https://quikpadvora.be/
Optional but of course nice to have if you could propose some design or guidance for Contact, About, and Conditions pages...
Here attached a full screen sequence.
Updates
Thanks for all your proposals ! They were submitted to the final customer, he selects one ASAP !
Number of Pages Required
3 page
Look and feel
Each slider illustrates characteristics of the customer's brand and the style your logo design should communicate.

```html
<!DOCTYPE html>
<html lang="en">
<head>
<meta charset="utf-8">
<title>New order – Location</title>
<link rel="stylesheet" href="https://fonts.googleapis.com/css2?family=Inter:wght@400;500;600&display=swap">
<style>
  :root {
    --brand-green: #48cb8f;
    --header-shadow: #d6d6d6;
    --pin-red: #ff0000;
    --field-bg: #e9eaed;
    --text-dark: #111111;
    --divider: #ececec;
    --action-blue: #47a4e9;
    --white: #ffffff;
  }
  * { box-sizing: border-box; margin: 0; padding: 0; }
  html, body {
    width: 674px;
    height: 1200px;
    overflow: hidden;
    background: var(--white);
    font-family: "Inter", sans-serif;
  }
  .screen {
    position: relative;
    width: 674px;
    height: 1200px;
    background: var(--white);
  }
  .app-header {
    position: absolute;
    left: 0; top: 0;
    width: 674px;
    height: 119px;
    background: var(--brand-green);
    border-bottom: 4px solid var(--header-shadow);
  }
  .back-link {
    position: absolute;
    left: 27px;
    top: 50px;
    display: flex;
    align-items: center;
    gap: 16px;
    color: var(--white);
    text-decoration: none;
    font-size: 38px;
    font-weight: 500;
    letter-spacing: 2px;
  }
  .back-link svg { width: 31px; height: 42px; }
  .location-pin {
    position: absolute;
    left: 89px;
    top: 211px;
    width: 57px;
    height: 81px;
  }
  .address-label {
    position: absolute;
    left: 200px;
    top: 229px;
    font-size: 33px;
    font-weight: 400;
    color: var(--text-dark);
    letter-spacing: 0.3px;
  }
  .address-field {
    position: absolute;
    background: var(--field-bg);
    border-radius: 8px;
    color: var(--text-dark);
    font-size: 31px;
    font-weight: 600;
    display: flex;
    align-items: center;
  }
  .field-number { left: 444px; top: 221px; width: 113px; height: 58px; justify-content: flex-end; padding-right: 25px; }
  .field-street { left: 199px; top: 303px; width: 357px; height: 57px; padding-left: 39px; }
  .field-city   { left: 200px; top: 385px; width: 357px; height: 57px; padding-left: 38px; }
  .section-divider {
    position: absolute;
    left: 67px;
    top: 481px;
    width: 541px;
    height: 1px;
    background: var(--divider);
  }
  .summary-button {
    position: absolute;
    left: 122px;
    top: 568px;
    width: 431px;
    height: 86px;
    background: var(--action-blue);
    border-radius: 8px;
    color: var(--white);
    text-decoration: none;
    display: flex;
    align-items: center;
    justify-content: center;
    gap: 20px;
    font-size: 42px;
    font-weight: 500;
    letter-spacing: 2.5px;
    padding-left: 8px;
  }
  .summary-button svg { width: 29px; height: 42px; }
</style>
</head>
<body>
  <main class="screen">
    <header class="app-header">
      <a class="back-link" href="#">
        <svg viewBox="0 0 31 42" aria-hidden="true">
          <polyline points="24,5 8,21 24,37" fill="none" stroke="#ffffff" stroke-width="9" stroke-linecap="round" stroke-linejoin="round"/>
        </svg>
        <span>Back</span>
      </a>
    </header>

    <svg class="location-pin" viewBox="0 0 57 81" aria-hidden="true">
      <path d="M28.5 0C12.8 0 0 12.6 0 28.2c0 6.2 2.3 11.6 5.5 16.6L28.5 81l23-36.2c3.2-5 5.5-10.4 5.5-16.6C57 12.6 44.2 0 28.5 0z" fill="#ff0000"/>
      <circle cx="28.5" cy="27" r="11" fill="#ffffff"/>
    </svg>

    <p class="address-label">At this address</p>
    <div class="address-field field-number">24</div>
    <div class="address-field field-street">Rue du vieux pont,</div>
    <div class="address-field field-city">1040 Valmorent</div>

    <div class="section-divider"></div>

    <a class="summary-button" href="#">
      <span>Summary</span>
      <svg viewBox="0 0 29 42" aria-hidden="true">
        <polyline points="7,6 22,21 7,36" fill="none" stroke="#ffffff" stroke-width="9" stroke-linecap="round" stroke-linejoin="round"/>
      </svg>
    </a>
  </main>
</body>
</html>
```